Snugpaw Emporium Click & Collect Service Flyer

We are a family owned and run pet shop in the UK and have been also selling online for 10 years. Our latest website launched last year is www.snugpawemporium.co.uk where we supply a large range of dog beds for delivery within the UK.
We require a two sided A6 flyer in portrait which will be given to customers in our shop and also at local pet events to advertise that they can now use our new 'Click & Collect' service to reserve a new dog bed from our online range and collect in store. The majority of these customers will be unaware of our website and the fact that we supply a much larger range of dog beds than they see within our store.
We would also like to use the flyer to direct customers to join our pallwire page.

Target Market(s)

UK adults aged 25-60, customers are now buying dog beds to suit their home decor.

Industry/Entity Type

Shop

Requirements
Must have
• two sides, A6 size in portrait, mention the Click & Collect service and how using this gives access to a wider range od beds than we have in store and also avoids delivery charges and waiting in for a delivery. Must have both logos and also pallwire logo. Website address www.snugpawemporium.co.uk
Nice to have
• a large image on the front with words something like 'Looking for a bigger range of dog beds?' for example, please feel free to suggest otherwise. On the reverse more info about the Click & Collect Service and our logos with a part about joing our pallwire page.
Should not have
• Cartoon style animals

```html
<!DOCTYPE html>
<html lang="en">
<head>
<meta charset="utf-8">
<title>Snugpaw Emporium – Click &amp; Collect Flyer</title>
<link rel="stylesheet" href="https://fonts.googleapis.com/css2?family=Archivo+Black&family=Arimo:ital,wght@0,400;0,700;1,400&family=Open+Sans:ital,wght@1,700&display=swap">
<style>
  :root {
    --brown: #4a2c1c;
    --brown-dark: #3a2114;
    --teal: #3cbfcc;
    --teal-light: #bfecef;
    --teal-pale: #e6f8f9;
    --ink: #1d1d1d;
    --grey: #cfcfcf;
    --grey-dark: #9a9a9a;
    --white: #ffffff;
    --page: #ffffff;
  }
  * { box-sizing: border-box; margin: 0; padding: 0; }
  html, body { width: 1200px; height: 840px; overflow: hidden; background: var(--page); }
  body { position: relative; font-family: "Arimo", Arial, sans-serif; color: var(--ink); }

  .side { position: absolute; top: 0; width: 595px; height: 840px; overflow: hidden; background: var(--white); }
  .side--front { left: 0; }
  .side--back { left: 605px; }

  .brand { position: absolute; left: 30px; font-family: "Arimo", Arial, sans-serif; font-weight: 700; color: var(--brown); line-height: 1; }
  .brand small { display: block; font-size: 15px; margin-bottom: 2px; }
  .brand span { font-size: 36px; letter-spacing: -0.5px; }

  .photo { position: absolute; }

  .tagline { position: absolute; left: 30px; top: 96px; font-family: "Open Sans", Arial, sans-serif; font-style: italic; font-weight: 700; font-size: 26px; line-height: 1.22; color: var(--brown); }

  .url-band { position: absolute; left: 0; width: 100%; background: linear-gradient(180deg, #6b4431, var(--brown) 55%, var(--brown-dark)); color: var(--white); font-weight: 700; font-family: "Arimo", Arial, sans-serif; text-shadow: 0 2px 2px rgba(0,0,0,.6); }

  .teal-panel { position: absolute; left: 0; width: 100%; background: linear-gradient(180deg, var(--teal) 0%, #6fd2db 45%, var(--teal-light) 100%); }

  .headline { position: absolute; font-family: "Archivo Black", Arial, sans-serif; color: #111; letter-spacing: -2px; text-shadow: 2px 2px 0 rgba(255,255,255,.5), 3px 4px 4px rgba(0,0,0,.35); white-space: nowrap; }
  .cursor { position: absolute; }

  .intro { position: absolute; left: 36px; top: 287px; width: 380px; font-style: italic; font-size: 15.5px; line-height: 1.3; color: #2a2a2a; }

  .footer { position: absolute; left: 0; bottom: 0; width: 100%; height: 72px; background: linear-gradient(180deg, #e4e4e4, var(--grey)); border-top: 2px solid var(--grey-dark); }
  .social { position: absolute; top: 16px; height: 38px; display: flex; align-items: center; gap: 6px; font-family: "Arimo", Arial, sans-serif; font-weight: 700; border-radius: 4px; padding: 0 10px; }
  .social--page { background: var(--white); border: 1px solid #999; color: var(--brown); font-size: 15px; }
  .social--page i { width: 22px; height: 22px; background: var(--brown); display: inline-block; }
  .social--follow { background: linear-gradient(180deg, #777, #444); color: var(--white); font-size: 14px; }

  .body-copy { position: absolute; left: 36px; top: 203px; width: 530px; font-size: 18px; line-height: 1.3; color: #1c1c1c; }
  .body-copy p { margin-bottom: 14px; }
  .body-copy h3 { font-size: 18px; font-weight: 700; margin: 18px 0 12px; }
  .body-copy .lead { font-weight: 700; margin-top: 4px; }
</style>
</head>
<body>

<!-- Front -->
<section class="side side--front">
  <div class="brand" style="top:22px"><small>The</small><span>Snugpaw Emporium</span></div>
  <p class="tagline">Looking for a Bigger range<br>of Dog beds?</p>
  <div class="photo" role="img" aria-label="Black terrier sitting on a grey paw-print dog bed" style="left:430px;top:0;width:165px;height:230px;background:radial-gradient(ellipse at 50% 70%, #9a9a9a, #d8d8d8 60%, #ffffff 85%)"></div>

  <div class="url-band" style="top:175px;height:66px;font-size:30px;padding:16px 0 0 38px">www.snugpawemporium.co.uk</div>

  <div class="teal-panel" style="top:241px;height:142px"></div>
  <h1 class="headline" style="left:36px;top:244px;font-size:50px">‘Click’&amp;Collect</h1>
  <svg class="cursor" style="left:12px;top:285px" width="26" height="30" viewBox="0 0 26 30"><path d="M2 2 L2 24 L8 18 L13 28 L17 26 L12 16 L21 16 Z" fill="#fff" stroke="#222" stroke-width="2"/></svg>
  <p class="intro">...allows you to reserve items from our huge online range and then call into our Ashcombe Green store to pay and collect your items.</p>
  <div class="photo" role="img" aria-label="White computer mouse" style="left:412px;top:262px;width:175px;height:118px;border-radius:50%;background:radial-gradient(ellipse at 40% 35%, #ffffff, #e6e6e6 60%, #b9c3c5)"></div>

  <div class="photo" role="img" aria-label="Golden retriever lying in a brown round dog bed beside a black and tan puppy on a cow-print cushion" style="left:0;top:383px;width:595px;height:387px;background:linear-gradient(135deg, #f5f0e8 0%, #d8b27a 30%, #7a4e2e 55%, #e7dccd 80%, #ffffff 100%)"></div>

  <footer class="footer">
    <div class="social social--page" style="left:256px"><i></i>pallwire</div>
    <div class="social social--follow" style="left:380px">FOLLOW US ON chirpline</div>
  </footer>
</section>

<!-- Back -->
<section class="side side--back">
  <div class="brand" style="top:20px"><small>The</small><span>Snugpaw Emporium</span></div>
  <div class="photo" role="img" aria-label="Black terrier sitting on a grey paw-print dog bed" style="left:415px;top:0;width:180px;height:135px;background:radial-gradient(ellipse at 55% 70%, #8e8e8e, #d6d6d6 60%, #ffffff 90%)"></div>

  <div class="url-band" style="top:80px;height:52px;font-size:28px;padding:11px 0 0 38px">www.snugpawemporium.co.uk</div>

  <div class="teal-panel" style="top:132px;height:638px;background:linear-gradient(180deg, var(--teal) 0%, #7fd6de 45%, var(--teal-pale) 100%)"></div>
  <h2 class="headline" style="left:30px;top:145px;font-size:42px">‘Click’&amp;Collect</h2>
  <svg class="cursor" style="left:18px;top:178px" width="22" height="26" viewBox="0 0 26 30"><path d="M2 2 L2 24 L8 18 L13 28 L17 26 L12 16 L21 16 Z" fill="#fff" stroke="#222" stroke-width="2"/></svg>

  <div class="body-copy">
    <p>Due to space limitations at our store we are unable to display the full range of beds and blankets that we supply. With our new Click &amp; Collect service local customers now have access to our full range online.</p>
    <p>Using our new <strong>Click &amp; Collect</strong> service means that you avoid paying delivery charges and you won't have to wait in for a delivery either.</p>
    <p class="lead">It's easy to do, just follow these three easy steps:</p>
    <h3>Step 1:</h3>
    <p>Browse our products and place any items you wish to purchase into the shopping cart. Checkout in the usual way filling in your details. Choose 'COLLECT FROM STORE' in the delivery method area.</p>
    <h3>Step 2:</h3>
    <p>We will email you as soon as your order<br>is ready for collection</p>
    <h3>Step 3:</h3>
    <p>Pop into our store in Maple Road,<br>Ashcombe Green to pay and collect your order</p>
  </div>
  <div class="photo" role="img" aria-label="White computer mouse" style="left:390px;top:555px;width:205px;height:205px;border-radius:50%;background:radial-gradient(ellipse at 40% 35%, #ffffff, #ececec 55%, #c3cbcd)"></div>

  <footer class="footer">
    <div class="social social--page" style="left:256px"><i></i>pallwire</div>
    <div class="social social--follow" style="left:380px">FOLLOW US ON chirpline</div>
  </footer>
</section>

</body>
</html>
```